Tovimerra: Travel business card redesign

We need a clean elegant look for our cards featuring blue and orange. Look should communicate a sense of strong design and seem uncluttered. The company is Tovimerra which means escape to bliss. As in every trip is an escape to bliss. Feel free to reinvent the logo or just tweak it. Colors should be blue like Caribbean waters and a saturated orange. Keep it clean and simple.
Please match the information in the sample uploaded but the sample is horrible -- a non-starter -- use for information only. also please add managing director to my name as title

Target Market(s)
potential clients, hotels, trade publications
Industry/Entity Type
Travel Industry
Contact Information for Business Card
as above
Requirements
Must have
- Font should be century gothic. Colors below are close but a but prefer lighter in each case.

```html
<!DOCTYPE html>
<html lang="en">
<head>
<meta charset="utf-8">
<title>Tovimerra business card</title>
<link href="https://fonts.googleapis.com/css2?family=Questrial&display=swap" rel="stylesheet">
<style>
  :root {
    --backdrop: #262628;
    --card: #2c2c2e;
    --card-edge: #3a3a3c;
    --orange: #f5922a;
    --blue: #5ab4e0;
    --white: #f2f2f2;
    --logo-emboss: #1c1c1d;
  }
  * { margin: 0; padding: 0; box-sizing: border-box; }
  html, body {
    width: 1200px; height: 1000px; overflow: hidden;
    background: var(--backdrop);
    font-family: "Questrial", "Century Gothic", sans-serif;
  }
  .card {
    position: absolute; left: 250px; width: 700px; height: 400px;
    background: var(--card);
    border: 1px solid var(--card-edge);
    box-shadow: 0 18px 40px rgba(0,0,0,.45);
  }
  .card--front { top: 60px; }
  .card--back { top: 540px; }

  .front-wordmark {
    position: absolute; top: 160px; left: 0; right: 0; text-align: center;
    font-size: 58px; color: var(--logo-emboss); letter-spacing: -1px; line-height: 1;
  }
  .front-motto {
    position: absolute; bottom: 56px; left: 0; right: 0; text-align: center;
    color: var(--orange); font-size: 19px; letter-spacing: 1px;
  }

  .holder { position: absolute; top: 44px; left: 44px; }
  .holder-name { font-size: 26px; letter-spacing: 2px; line-height: 1.1; }
  .holder-name .first { color: var(--orange); }
  .holder-name .last { color: var(--blue); }
  .holder-title { color: var(--white); font-size: 17px; margin-top: 2px; }

  .back-wordmark {
    position: absolute; top: 120px; right: 50px;
    font-size: 46px; color: var(--orange); line-height: 1; letter-spacing: -0.5px;
  }

  .contact-list { position: absolute; left: 44px; bottom: 40px; list-style: none; }
  .contact-list li {
    display: flex; align-items: center; gap: 12px;
    color: var(--white); font-size: 18px; line-height: 26px;
  }
  .contact-list svg { width: 14px; height: 14px; fill: var(--orange); }
  .contact-list .site .brand { color: var(--orange); }

  .address {
    position: absolute; right: 50px; bottom: 40px; text-align: right;
    color: var(--white); font-size: 18px; line-height: 26px; letter-spacing: 1px;
  }
</style>
</head>
<body>
  <section class="card card--front">
    <div class="front-wordmark">tovimerra</div>
    <p class="front-motto">journeys shaped around you</p>
  </section>

  <section class="card card--back">
    <div class="holder">
      <div class="holder-name"><span class="first">RAVEL</span> <span class="last">OSTIN</span></div>
      <div class="holder-title">Managing Director</div>
    </div>

    <div class="back-wordmark">tovimerra</div>

    <ul class="contact-list">
      <li><svg viewBox="0 0 16 16" aria-hidden="true"><path d="M3 1l3 3-1.5 2a9 9 0 005.5 5.5L12 10l3 3-2 2C7 15 1 9 1 3z"/></svg>855.46.(868637)</li>
      <li><svg viewBox="0 0 16 16" aria-hidden="true"><path d="M4 0h8a1 1 0 011 1v14a1 1 0 01-1 1H4a1 1 0 01-1-1V1a1 1 0 011-1zm1 2v10h6V2zm3 11a1 1 0 100 2 1 1 0 000-2z"/></svg>424.555.0182</li>
      <li><svg viewBox="0 0 16 16" aria-hidden="true"><path d="M4 0h8v5H4zM1 6h14v8H1zm3 2v2h8V8zM4 14h8v2H4z"/></svg>310.555.0147</li>
      <li><svg viewBox="0 0 16 16" aria-hidden="true"><circle cx="8" cy="8" r="8"/><path d="M0 8h16M8 0v16" stroke="#2c2c2e" stroke-width="1.2"/></svg><span class="site"><span class="brand">tovimerra</span>.com</span></li>
    </ul>

    <div class="address">
      1416 Harbor Crest Way N.<br>
      Marina Vista, 90412
    </div>
  </section>
</body>
</html>
```